"Freedom" New Year Electronic Card

Calventa is a regulatory consulting company in the cosmetic sector. We provide premium services and have 12 years of experience.

Please visit our website for more information: https://calventa.example

We need a graphic for a New Year electronic card to send to our clients (see brief attached):
- The attached picture shows the Holiday card we used before the Christmas break. We like the idea to make drawings with anonymized cosmetic packaging. We would like to do it with "2021".
- You can design a background (with nice shades of colors) but leave space at top and bottom for us to include text in different languages.
- We would like that the "1" of "2021" be a symbol of freedom. We thought about a dandelion and flying seeds (see brief) but you may propose something else (such as birds escaping a cage, broken chains, etc.)

We need something very professional, serious, beautiful and in line with our graphic layout (see our company website).

Target Market(s)

B2B professionals of the cosmetic industry

Requirements
Must have
• Symbol of freedom (dandelion, broken chain, birds escaping a cage, etc.)
Should not have
• Christmas-related things (no christmas trees, etc.)
No medical fatures (no seringes, etc.)

```html
<!DOCTYPE html>
<html lang="en">
<head>
<meta charset="utf-8">
<title>Calventa – New Year Card 2021</title>
<link rel="stylesheet" href="https://fonts.googleapis.com/css2?family=Arimo:wght@400;700&family=Oswald:wght@500&display=swap">
<style>
  :root {
    --backdrop: #e7e5e2;
    --card: #f5f5f5;
    --ink: #2a2a2a;
    --leaf: #9ccd5a;
    --leaf-deep: #8fc24d;
    --seed-light: #ffffff;
    --seed-shade: #e2ddd3;
  }
  html, body {
    margin: 0;
    width: 1200px;
    height: 900px;
    overflow: hidden;
    background: var(--backdrop);
  }
  .card {
    position: absolute;
    left: 45px;
    top: 80px;
    width: 1110px;
    height: 740px;
    background: var(--card);
    box-shadow: 0 6px 18px rgba(0,0,0,0.12);
    overflow: hidden;
  }
  .brand-name {
    position: absolute;
    top: 28px;
    left: 0;
    width: 100%;
    margin: 0;
    text-align: center;
    font-family: "Arimo", sans-serif;
    font-weight: 700;
    font-size: 96px;
    line-height: 1;
    letter-spacing: 1px;
    color: var(--ink);
  }
  .year {
    position: absolute;
    left: 0;
    top: 0;
    width: 1110px;
    height: 740px;
  }
  .year text {
    font-family: "Oswald", sans-serif;
    font-weight: 500;
    font-size: 384px;
    fill: var(--leaf);
  }
  .freedom-symbol {
    position: absolute;
    left: 705px;
    top: 163px;
    width: 190px;
    height: 343px;
    background: radial-gradient(circle at 50% 28%, var(--seed-light) 0%, var(--seed-shade) 28%, rgba(226,221,211,0) 30%),
                linear-gradient(to bottom, rgba(0,0,0,0) 45%, rgba(188,214,150,0.55) 46%, rgba(188,214,150,0.55) 100%);
    background-size: 100% 100%, 10px 100%;
    background-position: 0 0, 45% 0;
    background-repeat: no-repeat;
  }
  .message {
    position: absolute;
    top: 530px;
    left: 0;
    width: 100%;
    margin: 0;
    text-align: center;
    font-family: "Arimo", sans-serif;
    font-size: 17px;
    line-height: 22px;
    color: var(--ink);
  }
  .meadow {
    position: absolute;
    left: 0;
    bottom: 0;
    width: 100%;
    height: 125px;
    background: linear-gradient(to bottom, rgba(156,205,90,0) 0%, rgba(156,205,90,0.7) 30%, var(--leaf-deep) 55%, var(--leaf) 100%);
  }
</style>
</head>
<body>
  <main class="card">
    <h1 class="brand-name">calventa</h1>
    <svg class="year" viewBox="0 0 1110 740" aria-label="2021">
      <text x="243" y="490" textLength="478" lengthAdjust="spacingAndGlyphs">202</text>
    </svg>
    <div class="freedom-symbol" role="img" aria-label="Dandelion seed head on a slender stem, standing as the 1 of 2021"></div>
    <p class="message">
      Lorem ipsum dolor sit amet, consectetuer adipiscing elit, sed diam nonummy nibh euismod<br>
      tincidunt ut laoreet dolore magna aliquam erat volutpat. Ut wisi enim ad minim veniam, quis<br>
      nostrud exerci tation ullamcorper suscipit lobortis nisl ut aliquip ex ea commodo consequat.<br>
      Duis autem vel elit, sed diam nonummy nibh euismod tincidunt ut laoreet
    </p>
    <div class="meadow" role="img" aria-label="Green grass silhouette along the bottom edge"></div>
  </main>
</body>
</html>
```